Online Book Sale Postcard Design

I need a postcard design to announce the online sale of my paperback book listed on Trovaly.com and Pagebrook.com. My book is about Christmas and belief in God told in short stories, poems, and prayer to help individuals, children, and families celebrate Christmas.
I live in Houston, TX with my retired parents and younger sister in our neighborhood that has a lot of retired citizens and neighbors. The book is a tribute to the neighborhood which is the source of inspiration for the poem which has the same title as the book "Humming Bells, Drifting Snow." I wrote that poem in 2001 after a car tour of the neighborhood in December of 2000.
This is my first book that I've written and is listed on Trovaly.com and PageBrook.com. I have a high resolution cover jpeg upload that I would like to use on the front (full color) of the postcard. The basic information showing when it's for sale and where it can be bought is what I need printed on the postcard. I have marketing copy that can be used, also. I want the postcard to convey joy and cheer to communicate the mood of the season as well as of the book, "Humming Bells, Drifting Snow."
Target Market(s)
Females aged 35+, influenced by husbands and young children, teenagers, and young adults.
Industry/Entity Type
Marketing
Requirements
Nice to have
- I trust your creative judgment. Something that makes homeowners want to keep the postcard for reference and as a reminder to buy for themselves and/or give as a gift.
Should not have
- Don't crowd the postcard with too much information. Specifics is all that's needed. I trust your judgment.

```html
<!DOCTYPE html>
<html lang="en">
<head>
<meta charset="utf-8">
<title>Humming Bells, Drifting Snow – Postcard</title>
<link rel="stylesheet" href="https://fonts.googleapis.com/css2?family=Open+Sans:ital,wght@0,300;0,400;0,600;1,400;1,600&display=swap">
<style>
  :root {
    --stage: #7a5232;
    --navy: #26286e;
    --navy-light: #4a4ea0;
    --green: #3d7a4c;
    --gold: #ecd9a0;
    --gold-deep: #c9ad6a;
    --cream: #f3e08a;
    --red: #e8262c;
    --white: #ffffff;
    --ink: #111111;
    --text-green: #2f6a3c;
  }
  * { box-sizing: border-box; margin: 0; padding: 0; }
  html, body { width: 781px; height: 1200px; overflow: hidden; }
  body {
    position: relative;
    background: var(--stage);
    font-family: "Open Sans", Arial, sans-serif;
  }
  .card { position: absolute; overflow: hidden; }
  .card svg.card-art { position: absolute; inset: 0; display: block; }

  /* Front */
  .front { left: 42px; top: 47px; width: 679px; height: 526px; }
  .front .headline-online {
    position: absolute; left: 70px; top: 58px;
    font-size: 60px; font-weight: 300; color: var(--cream); letter-spacing: 1px; line-height: 1;
  }
  .front .headline-sale {
    position: absolute; left: 66px; top: 130px;
    font-size: 94px; font-weight: 300; color: var(--red); line-height: 1;
  }
  .front .book-title {
    position: absolute; right: 328px; top: 362px; text-align: right;
    color: var(--white); font-size: 35px; line-height: 58px; font-weight: 400;
    white-space: nowrap;
  }
  .front .book-title em { font-style: italic; }
  .front .where-to-buy {
    position: absolute; left: 21px; top: 476px;
    font-size: 19px; color: var(--cream); font-weight: 400;
  }

  /* Back */
  .back { left: 50px; top: 622px; width: 681px; height: 528px; }
  .back .blurb {
    position: absolute; left: 22px; top: 26px; width: 275px;
    font-size: 14.6px; line-height: 21.7px; color: var(--white); font-weight: 300;
  }
  .back .listing {
    position: absolute; left: 22px; top: 286px; width: 290px; height: 162px;
    border-radius: 30px;
    background: linear-gradient(120deg, #b69a5c, #f1e2b4 45%, #c7a866);
    text-align: center; padding-top: 4px;
  }
  .listing .label { font-size: 19px; color: var(--text-green); line-height: 22px; }
  .listing .store { font-size: 26px; color: var(--navy); line-height: 29px; }
  .listing .label.second { margin-top: 8px; }
  .listing .store.caps { font-size: 27px; }
  .back .contact-line {
    position: absolute; left: 43px; top: 454px;
    font-size: 18px; color: var(--white);
  }
  .back .phone {
    position: absolute; left: 43px; top: 476px;
    font-size: 30px; font-weight: 600; color: var(--gold); display: flex; align-items: center; gap: 8px;
  }
  .back .address {
    position: absolute; left: 331px; top: 88px;
    font-size: 14.5px; color: var(--ink); line-height: 20px;
  }
  .address .title-line { font-style: italic; }
  .address .title-line span { font-style: normal; }
  .address .street { padding-left: 58px; }
  .back .stamp-box {
    position: absolute; left: 588px; top: 94px; width: 54px; height: 70px;
    border: 1.5px solid var(--ink);
  }
  .back .address-rule {
    position: absolute; left: 433px; width: 209px; height: 1.5px; background: var(--ink);
  }
</style>
</head>
<body>

<section class="card front" aria-label="Postcard front">
  <svg class="card-art" viewBox="0 0 679 526" aria-hidden="true">
    <defs>
      <radialGradient id="navyGlow" cx="45%" cy="35%" r="70%">
        <stop offset="0" stop-color="#4f53a6"/>
        <stop offset="1" stop-color="#25276d"/>
      </radialGradient>
      <linearGradient id="greenSweep" x1="0" y1="0" x2="0" y2="1">
        <stop offset="0" stop-color="#3f7d4e"/>
        <stop offset="1" stop-color="#356c43"/>
      </linearGradient>
    </defs>
    <rect width="679" height="526" fill="url(#navyGlow)"/>
    <path d="M0 150 C200 190 420 330 679 395 L679 526 L0 526 Z" fill="url(#greenSweep)"/>
    <path d="M360 470 C480 430 580 415 679 420 L679 450 C580 445 480 460 360 500 Z" fill="#2b2d72"/>
    <path d="M0 178 C200 215 400 325 679 318" fill="none" stroke="#ecd9a0" stroke-width="2.5"/>
    <path d="M0 200 C210 260 420 360 679 432" fill="none" stroke="#ecd9a0" stroke-width="2"/>
  </svg>

  <div role="img" aria-label="Book cover of Humming Bells, Drifting Snow by Marla J. Dunmore, shown standing upright"
       style="position:absolute; left:378px; top:14px; width:252px; height:484px;
              background:linear-gradient(160deg,#f4ead0,#d8c28f 55%,#efe3c2); box-shadow:6px 6px 14px rgba(0,0,0,.35);"></div>
  <div aria-hidden="true" style="position:absolute; left:630px; top:10px; width:9px; height:488px; background:#f7f7f7;"></div>

  <div class="headline-online">ONLINE</div>
  <div class="headline-sale">SALE</div>
  <div class="book-title"><em>Humming</em> BELLS,<br><em>Drifting</em> SNOW</div>
  <div class="where-to-buy">ON TROVALY.COM &amp; PAGEBROOK.COM</div>
</section>

<section class="card back" aria-label="Postcard back">
  <svg class="card-art" viewBox="0 0 681 528" aria-hidden="true">
    <defs>
      <radialGradient id="backGlow" cx="25%" cy="55%" r="70%">
        <stop offset="0" stop-color="#3d4196"/>
        <stop offset="1" stop-color="#24266b"/>
      </radialGradient>
    </defs>
    <rect width="681" height="528" fill="url(#backGlow)"/>
    <path d="M325 0 L681 0 L681 528 L490 528 C385 420 305 220 325 0 Z" fill="#ffffff"/>
    <path d="M312 0 C294 220 372 420 468 528" fill="none" stroke="#ecd9a0" stroke-width="2.5"/>
    <path d="M323 0 C303 220 380 420 482 528" fill="none" stroke="#ecd9a0" stroke-width="1.5"/>
  </svg>

  <p class="blurb">"Humming Bells, Drifting Snow" shares my thoughts about Christmas and belief in God told in short stories, poems, and prayer. The poem of the same title pays tribute to Maple Hollow, my childhood home which is still my home as an adult. Discover "Humming Bells, Drifting Snow" in one shining moment after shining moment of joy, praise of God's Spirit and prayer.</p>

  <div class="listing">
    <div class="label">LISTED ON</div>
    <div class="store">Trovaly.com</div>
    <div class="store">PageBrook.com</div>
    <div class="label second">ALSO AVAILABLE AT</div>
    <div class="store caps">QUILLMARK BOOKS</div>
  </div>

  <div class="contact-line">For information call Marla</div>
  <div class="phone">
    <svg width="20" height="26" viewBox="0 0 20 26" aria-hidden="true">
      <rect x="1" y="1" width="18" height="24" rx="3" fill="#ecd9a0"/>
      <rect x="4" y="4" width="12" height="6" fill="#2a2c70"/>
      <g fill="#2a2c70">
        <rect x="4" y="13" width="3" height="3"/><rect x="8.5" y="13" width="3" height="3"/><rect x="13" y="13" width="3" height="3"/>
        <rect x="4" y="18" width="3" height="3"/><rect x="8.5" y="18" width="3" height="3"/><rect x="13" y="18" width="3" height="3"/>
      </g>
    </svg>
    555-014-2290
  </div>

  <div class="address">
    <div class="title-line">“Humming <span>Bells</span> Drifting <span>Snow</span>”</div>
    <div class="street">4127 Larkspur<br>Street/Houston,<br>TX 77041</div>
  </div>
  <div class="stamp-box" aria-label="Stamp area"></div>
  <div class="address-rule" style="top:281px"></div>
  <div class="address-rule" style="top:312px"></div>
  <div class="address-rule" style="top:344px"></div>
</section>

</body>
</html>
```